I am a business consultant/coach and I am branding myself 'The Zero Fee Venture Mentor'. My business name is Bright Harbor Advisory.I want an oversized postcard designed for lead generation. It will be sent through the post so will require area for an address and stamp The details that I want on the card are attached plus a photo of myself. Also I have attached a copy of my business card so that you are able to see the style and colors I use. I would like the main headline to be bold red, or bold red background Hope this is enough info.
Target Market(s)
Owners/managers of medium sized businesses
Industry/Entity Type
Business Consultant
Requirements
Must have
- The cards I want to be noticed and professional in appearance, they will be use dfor lead generation and sent through the postal service
Nice to have
- The colors that I use on my business cards are green, grey and white. I want the main headline to be in red or red backgroun dso that it stands out
Should not have
- The words that I have used are basically off my landing page for consistency

```html
<!DOCTYPE html>
<html lang="en">
<head>
<meta charset="utf-8">
<title>Zero Fee Venture Mentor – Postcard Back</title>
<link rel="stylesheet" href="https://fonts.googleapis.com/css2?family=Montserrat:wght@700;800&family=Arimo&display=swap">
<style>
  :root {
    --red: #c40000;
    --red-mid: #a80000;
    --red-dark: #7e0000;
    --frame: #3a0000;
    --green: #46ff00;
    --green-soft: #3fd400;
    --grey: #bccacf;
    --paper: #edf2f3;
    --ink: #1c1c1c;
    --white: #ffffff;
  }
  html, body {
    margin: 0;
    padding: 0;
    width: 1200px;
    height: 930px;
    overflow: hidden;
    background: var(--red);
  }
  .postcard {
    position: relative;
    width: 1200px;
    height: 930px;
    overflow: hidden;
    font-family: "Arimo", Arial, sans-serif;
    color: var(--ink);
  }
  .backdrop {
    position: absolute;
    inset: 0;
    background:
      radial-gradient(ellipse 160px 90px at 1000px 90px, var(--red-dark), transparent 70%),
      radial-gradient(ellipse 220px 120px at 820px 420px, rgba(126,0,0,.55), transparent 70%),
      radial-gradient(ellipse 140px 60px at 470px 380px, rgba(126,0,0,.6), transparent 70%),
      radial-gradient(ellipse 120px 50px at 470px 730px, rgba(110,0,0,.7), transparent 70%),
      radial-gradient(ellipse 260px 160px at 1080px 640px, rgba(140,0,0,.5), transparent 70%),
      radial-gradient(ellipse 300px 200px at 200px 800px, rgba(160,0,0,.5), transparent 70%),
      linear-gradient(180deg, var(--red) 0%, var(--red-mid) 100%);
  }
  .frame-outer {
    position: absolute;
    left: 10px; top: 10px; right: 10px; bottom: 10px;
    border: 8px solid rgba(150,0,0,.8);
  }
  .frame-inner {
    position: absolute;
    left: 26px; top: 26px;
    width: 1140px; height: 874px;
    border: 6px solid var(--frame);
    box-sizing: border-box;
  }
  .offer-card {
    position: absolute;
    left: 0; top: 0;
    width: 902px;
    font-family: "Montserrat", Arial, sans-serif;
    font-weight: 800;
    text-align: center;
  }
  .offer-card__fade {
    height: 30px;
    background: linear-gradient(90deg, var(--green-soft), #5ad000 60%, rgba(70,200,0,.6));
  }
  .offer-card__title {
    height: 30px;
    line-height: 31px;
    background: var(--green);
    color: var(--white);
    font-size: 18px;
    letter-spacing: 2px;
    text-transform: uppercase;
  }
  .offer-card__contact {
    height: 98px;
    background: var(--grey);
    box-sizing: border-box;
    padding-top: 11px;
    font-size: 14px;
    letter-spacing: 1px;
    line-height: 13.6px;
  }
  .offer-card__contact .tagline { margin-bottom: 7px; }
  .offer-card__guarantee {
    height: 108px;
    background: var(--paper);
    box-sizing: border-box;
    padding-top: 13px;
  }
  .offer-card__heading {
    font-size: 19px;
    letter-spacing: 1.4px;
    margin-bottom: 9px;
  }
  .offer-card__quote {
    font-size: 16px;
    letter-spacing: 1.2px;
    line-height: 16.4px;
    margin: 0;
  }
  .offer-card__link {
    height: 32px;
    line-height: 32px;
    background: var(--green);
    color: var(--white);
    font-size: 19px;
    letter-spacing: 1.4px;
  }
  .zone-label {
    position: absolute;
    font-size: 35px;
    line-height: 42px;
    text-align: center;
    color: var(--ink);
  }
  .zone-label--postage { left: 958px; top: 120px; width: 160px; }
  .zone-label--address { left: 740px; top: 364px; width: 276px; }
  .zone-label--barcode { left: 536px; top: 818px; width: 276px; }
  .zone-note {
    position: absolute;
    top: 464px;
    font-size: 24px;
    line-height: 30.4px;
    margin: 0;
    color: var(--ink);
  }
  .zone-note--left { left: 78px; width: 470px; }
  .zone-note--right { left: 642px; width: 480px; }
</style>
</head>
<body>
<div class="postcard">
  <div class="backdrop" role="img" aria-label="Softly blurred portrait photograph of the mentor in a red duotone, used as the card background"></div>
  <div class="frame-outer"></div>
  <div class="frame-inner"></div>

  <section class="offer-card">
    <div class="offer-card__fade"></div>
    <div class="offer-card__title">Zero Fee Venture Mentor</div>
    <div class="offer-card__contact">
      <div class="tagline">Commited to your Success</div>
      <div>Any questions? Contact me</div>
      <div>Daniel Ashcombe</div>
      <div>Bright Harbor Advisory</div>
      <div>0400 518 273</div>
    </div>
    <div class="offer-card__guarantee">
      <div class="offer-card__heading">Special Offer - My Guarantee</div>
      <p class="offer-card__quote">“If I cannot uncover at least 5 times my fee from<br>potential profits hidden within your business<br>after one interview then it is free.”</p>
    </div>
    <div class="offer-card__link">visit brightharbor.com.au/zerofee</div>
  </section>

  <div class="zone-label zone-label--postage">Postage<br>Area</div>
  <div class="zone-label zone-label--address">Address Area</div>
  <div class="zone-label zone-label--barcode">Barcode Area</div>

  <p class="zone-note zone-note--left">This zone should contain no addresses that include a zip code or state. The Post Office will scan this entire area for recipient addresses and zip codes.</p>
  <p class="zone-note zone-note--right">The only text allowed in the Address Area<br>is the recipient mailing address.<br>Red zones may have no text or<br>graphics darker than 7% grayscale.</p>
</div>
</body>
</html>
```